Legal Service Estimated Retainer and Average Case Value

We need an 11x14 flyer that contains the standard retainers and average cost be case, both provided in documents, for each case type we handle. We need the information displayed, preferably in a way that makes the information readable but less troubling to a client shocked at price of litigation. We need one sheet with the retainers and average case value merged into one table.

Target Market(s)

Potential Clients

Font styles to use
Serif
Sans Serif

```html
<!DOCTYPE html>
<html lang="en">
<head>
<meta charset="utf-8">
<title>Family Law Fee Flyer</title>
<link rel="stylesheet" href="https://fonts.googleapis.com/css2?family=Cinzel:wght@400;600;700&family=Crimson+Pro:wght@400;600;700&display=swap">
<style>
  :root{
    --navy:#0c1a4b;
    --navy-deep:#08133a;
    --ink:#1e2233;
    --row-dark:#e3e4e7;
    --row-light:#f3f3f4;
    --panel:#e9eaec;
    --charcoal:#2c2c2e;
    --white:#ffffff;
  }
  *{margin:0;padding:0;box-sizing:border-box}
  html,body{width:758px;height:1200px;overflow:hidden;background:#fff}
  .flyer{position:relative;width:758px;height:1200px;background:var(--white);font-family:"Crimson Pro",Georgia,serif;color:var(--ink)}

  /* header */
  .hero{position:absolute;left:0;top:0;width:758px;height:390px;
    background:linear-gradient(100deg,#f1f1f2 0%,#dcdcdf 45%,#c9c7c3 70%,#b9b5ae 100%)}
  .hero-backdrop{position:absolute;left:150px;top:60px;width:300px;height:320px;border-radius:50%;
    background:radial-gradient(circle,rgba(120,110,95,.25),rgba(120,110,95,0) 70%)}
  .portrait{position:absolute;left:456px;top:0;width:302px;height:390px;
    background:linear-gradient(180deg,#8e8e92 0%,#6d6e74 45%,#2a2f45 75%,#151a2e 100%)}
  .brand{position:absolute;left:45px;top:44px;display:flex;align-items:center;gap:10px}
  .brand-mark{width:28px;height:28px;background:var(--navy)}
  .brand-name{font-family:"Cinzel",serif;font-weight:400;color:var(--navy);font-size:17px;line-height:1;letter-spacing:.3px}
  .headline{position:absolute;left:45px;top:160px;font-family:"Cinzel",serif;color:var(--navy-deep);line-height:1}
  .headline .small{display:block;font-size:36px;font-weight:400;letter-spacing:.5px;margin-bottom:8px}
  .headline .big{display:block;font-size:62px;font-weight:700;color:var(--navy);margin-top:4px}
  .rule{position:absolute;left:45px;top:354px;width:250px;height:1px;background:#5a5f72}
  .rule::before{content:"";position:absolute;left:0;top:-2px;width:45px;height:5px;background:var(--navy);border-radius:2px}
  .hero-bar{position:absolute;left:0;top:390px;width:758px;height:5px;background:var(--navy)}

  /* fee table */
  .section-title{font-family:"Cinzel",serif;font-weight:400;font-size:21px;color:var(--navy);font-variant:small-caps;letter-spacing:.4px}
  .fees{position:absolute;left:45px;top:428px;width:333px}
  .fees .section-title::after{content:"";display:block;width:95px;height:2px;background:var(--navy);margin-top:10px}
  .intro{margin-top:16px;font-size:11.2px;line-height:1.27;color:#333}
  .fee-table{position:absolute;left:45px;top:562px;width:333px;height:557px;display:flex;flex-direction:column}
  .fee-table .row{display:flex;align-items:center;padding:0 10px 0 8px;font-size:11px;font-weight:700;flex:1}
  .fee-table .row.tall{flex:1.35}
  .fee-table .row:nth-child(odd){background:var(--row-dark)}
  .fee-table .row:nth-child(even){background:var(--row-light)}
  .tick{width:12px;height:12px;flex:none;margin-right:12px}
  .fee-table .label{flex:1;line-height:1.15}
  .fee-table .amount{width:84px;flex:none}

  /* retainer panel */
  .retainers{position:absolute;left:405px;top:395px;width:310px;height:724px;background:var(--panel);border-radius:0 0 10px 10px}
  .retainers-head{height:163px;background:var(--navy);padding:44px 16px 0 28px}
  .retainers-head .section-title{color:#fff;font-size:24px;line-height:1.25}
  .retainers-head .section-title::after{content:"";display:block;width:150px;height:2px;background:#fff;margin-top:14px}
  .retainer-table{display:flex;flex-direction:column;height:552px}
  .retainer-table .row{display:flex;align-items:center;padding:0 8px 0 30px;font-size:11px;font-weight:600;flex:1;border-bottom:1.5px solid var(--navy)}
  .retainer-table .row:nth-child(odd){background:#e1e2e6}
  .retainer-table .row:nth-child(even){background:#eeeff1}
  .retainer-table .row.tall{flex:1.4}
  .retainer-table .row.taller{flex:1.9}
  .retainer-table .row:last-child{border-bottom:none;border-radius:0 0 10px 10px}
  .retainer-table .tick{margin-right:12px}
  .retainer-table .label{flex:1;line-height:1.15}
  .retainer-table .key{width:70px;flex:none}
  .retainer-table .value{width:48px;flex:none}
  .retainer-table .full{flex:none}

  /* footer */
  .footer-info{position:absolute;left:0;top:1150px;width:758px;height:50px;background:var(--charcoal);color:#fff;
    display:flex;align-items:center;justify-content:flex-end;padding-right:42px;gap:14px;font-size:13px}
  .footer-info svg{width:13px;height:13px;margin-right:8px;vertical-align:-2px}
  .footer-info .sep{opacity:.8}
  .footer-call{position:absolute;left:0;top:1139px;width:320px;height:61px;background:var(--navy);
    clip-path:polygon(0 0,300px 0,320px 100%,0 100%);color:#fff;display:flex;align-items:center;padding-left:45px;gap:14px}
  .footer-call .call{font-family:"Cinzel",serif;font-weight:700;font-size:19px;letter-spacing:.5px}
  .footer-call .phone{font-family:"Cinzel",serif;font-size:23px;font-weight:400}
</style>
</head>
<body>
<svg width="0" height="0" style="position:absolute">
  <symbol id="tick-icon" viewBox="0 0 12 12">
    <circle cx="6" cy="6" r="5" fill="none" stroke="#0c1a4b" stroke-width="1.6"/>
    <path d="M3.3 6.1 L5.3 8 L10.5 2.5" fill="none" stroke="#0c1a4b" stroke-width="1.8" stroke-linecap="round"/>
  </symbol>
</svg>

<main class="flyer">
  <header class="hero">
    <div class="hero-backdrop" role="img" aria-label="Soft background photo of a gavel and legal papers"></div>
    <div class="portrait" role="img" aria-label="Portrait photo of the attorney in a dark suit"></div>
    <div class="brand">
      <span class="brand-mark"></span>
      <span class="brand-name">MILES T HARROW</span>
    </div>
    <h1 class="headline">
      <span class="small">CENTRAL PA'S</span>
      <span class="small">PREMIER FAMILY</span>
      <span class="big">LAW FIRM</span>
    </h1>
    <div class="rule"></div>
  </header>
  <div class="hero-bar"></div>

  <section class="fees">
    <h2 class="section-title">Average Fee Per Case Type</h2>
    <p class="intro">In order for our clients to set expectations for legal fees, we provide the national average range of fees per case type. These are only to provide you with an understanding of what other cases have cost clients in similar cases. Please note these are not estimates nor guarantees of your own legal costs.</p>
  </section>

  <div class="fee-table">
    <div class="row"><svg class="tick"><use href="#tick-icon"/></svg><span class="label">Custody Contempt/Modification</span><span class="amount">$5,000 - $8,000</span></div>
    <div class="row"><svg class="tick"><use href="#tick-icon"/></svg><span class="label">Custody Initial Order</span><span class="amount">$4,000 - $7,000</span></div>
    <div class="row"><svg class="tick"><use href="#tick-icon"/></svg><span class="label">Custody &amp; Support</span><span class="amount">$5,000 - $8,000</span></div>
    <div class="row"><svg class="tick"><use href="#tick-icon"/></svg><span class="label">Support</span><span class="amount">$2,000 - $4,000</span></div>
    <div class="row"><svg class="tick"><use href="#tick-icon"/></svg><span class="label">Divorce (3301c)</span><span class="amount">$1,500 - $3,000</span></div>
    <div class="row"><svg class="tick"><use href="#tick-icon"/></svg><span class="label">Divorce (3301d)</span><span class="amount">$2,000 - $3,000</span></div>
    <div class="row"><svg class="tick"><use href="#tick-icon"/></svg><span class="label">Protection from Abuse</span><span class="amount">$1,500 - $3,000</span></div>
    <div class="row"><svg class="tick"><use href="#tick-icon"/></svg><span class="label">Divorce &amp; Custody</span><span class="amount">$5,000 - $8,000</span></div>
    <div class="row tall"><svg class="tick"><use href="#tick-icon"/></svg><span class="label">Divorce &amp; Equitable<br>Distribution</span><span class="amount">$6,000 - $10,000</span></div>
    <div class="row"><svg class="tick"><use href="#tick-icon"/></svg><span class="label">Divorce, Custody &amp; Support</span><span class="amount">$8,000 - $12,000</span></div>
    <div class="row tall"><svg class="tick"><use href="#tick-icon"/></svg><span class="label">Divorce, Equitable Distribution<br>&amp; Custody</span><span class="amount">$10,000 - $15,000</span></div>
    <div class="row tall"><svg class="tick"><use href="#tick-icon"/></svg><span class="label">Divorce, Equitable Distribution<br>&amp; Support</span><span class="amount">$8,000 - $12,000</span></div>
    <div class="row tall"><svg class="tick"><use href="#tick-icon"/></svg><span class="label">Divorce, Equitable Distribution,<br>Custody &amp; Support</span><span class="amount">$12,000 - $15,000</span></div>
  </div>

  <section class="retainers">
    <div class="retainers-head">
      <h2 class="section-title">Retainers and Total Estimated Case Costs:</h2>
    </div>
    <div class="retainer-table">
      <div class="row"><svg class="tick"><use href="#tick-icon"/></svg><span class="label">Divorce (3301 C):</span><span class="key">Retainer:</span><span class="value">$2,000</span></div>
      <div class="row"><svg class="tick"><use href="#tick-icon"/></svg><span class="label">Divorce (3301 D):</span><span class="key">Retainer:</span><span class="value">$2,500</span></div>
      <div class="row"><svg class="tick"><use href="#tick-icon"/></svg><span class="label">Divorce and Custody:</span><span class="key">Retainer:</span><span class="value">$3,500</span></div>
      <div class="row tall"><svg class="tick"><use href="#tick-icon"/></svg><span class="label">Divorce and Equitable<br>Distribution:</span><span class="key">Retainer:</span><span class="value">$3,500</span></div>
      <div class="row"><svg class="tick"><use href="#tick-icon"/></svg><span class="label">Divorce and Support:</span><span class="key">Retainer:</span><span class="value">$3,000</span></div>
      <div class="row tall"><svg class="tick"><use href="#tick-icon"/></svg><span class="label">Divorce, Custody and<br>Support:</span><span class="key">Retainer:</span><span class="value">$3,500</span></div>
      <div class="row tall"><svg class="tick"><use href="#tick-icon"/></svg><span class="label">Divorce, Equitable<br>Distribution and Support:</span><span class="key">Retainer:</span><span class="value">$3,500</span></div>
      <div class="row tall"><svg class="tick"><use href="#tick-icon"/></svg><span class="label">Divorce, Equitable<br>Distribution and Custody:</span><span class="key">Retainer:</span><span class="value">$5,000</span></div>
      <div class="row taller"><svg class="tick"><use href="#tick-icon"/></svg><span class="label">Divorce, Equitable<br>Distribution, Custody<br>and Support:</span><span class="key">Retainer:</span><span class="value">$3,500</span></div>
      <div class="row"><svg class="tick"><use href="#tick-icon"/></svg><span class="label">Custody Initial Order:</span><span class="key">Retainer:</span><span class="value">$3,000</span></div>
      <div class="row"><svg class="tick"><use href="#tick-icon"/></svg><span class="label">Custody Modification:</span><span class="key">Retainer:</span><span class="value">$3,500</span></div>
      <div class="row"><svg class="tick"><use href="#tick-icon"/></svg><span class="label">Custody and Support:</span><span class="key">Retainer:</span><span class="value">$3,000</span></div>
      <div class="row"><svg class="tick"><use href="#tick-icon"/></svg><span class="label">(PFA) Protection From Abuse:</span><span class="full">$2,000 Paid In Full</span></div>
    </div>
  </section>

  <footer>
    <div class="footer-info">
      <span><svg viewBox="0 0 13 13"><rect x="1" y="3" width="11" height="7.5" fill="#fff"/><path d="M1 3 L6.5 7.5 L12 3" fill="none" stroke="#2c2c2e" stroke-width="1.2"/></svg>info@harrowfamilylaw.com</span>
      <span class="sep">|</span>
      <span><svg viewBox="0 0 13 13"><circle cx="6.5" cy="6.5" r="5.5" fill="none" stroke="#fff" stroke-width="1.2"/><ellipse cx="6.5" cy="6.5" rx="2.4" ry="5.5" fill="none" stroke="#fff" stroke-width="1"/><path d="M1 6.5 H12" stroke="#fff" stroke-width="1"/></svg>www.harrowfamilylaw.com</span>
    </div>
    <div class="footer-call">
      <span class="call">CALL US</span>
      <span class="phone">(555)204-7391</span>
    </div>
  </footer>
</main>
</body>
</html>
```